Owner of Clinical Testing Lab/. Pixel Harbor Logo completed. Need Matching business Cards

Im the owner of and need cards for business. Colors fonts and logo already purchased through pixel harbor and have the source files. Like to keep same color format , Include logo one side. My Name Address of Lab. My cell number, Lab telephone number and website address. Want to keep simple.

Target Market(s)

Customers

Industry/Entity Type

HealthCare

Contact Information for Business Card

Dr. Corisande Threlkeld Ph.D. Address: QVT Foundry Campus 4417 Foundry Campus Loop Building 2600 Room 314. Baton Rouge LA 70931. Phone : 555.317.0942

Requirements
Must have
• Logo - Color same

```html
<!DOCTYPE html>
<html lang="en">
<head>
<meta charset="utf-8">
<title>Business Card – Dr. Corisande Threlkeld</title>
<link rel="stylesheet" href="https://fonts.googleapis.com/css2?family=Montserrat:wght@400;500;700&display=swap">
<style>
  :root {
    --navy: #2c5888;
    --teal: #5fc3ab;
    --white: #ffffff;
    --stage: #f2f3f5;
    --shadow: rgba(20, 40, 70, 0.16);
  }
  * { box-sizing: border-box; margin: 0; padding: 0; }
  html, body {
    width: 1200px;
    height: 1200px;
    overflow: hidden;
    background: var(--stage);
    font-family: "Montserrat", Arial, sans-serif;
  }
  .sheet {
    width: 1200px;
    height: 1200px;
    display: flex;
    flex-direction: column;
    align-items: center;
    justify-content: center;
    gap: 60px;
  }
  .card {
    position: relative;
    width: 840px;
    height: 510px;
    box-shadow: 6px 8px 18px var(--shadow);
    overflow: hidden;
  }

  /* Front */
  .card--front {
    background: var(--navy);
    display: flex;
    flex-direction: column;
  }
  .card__name {
    height: 310px;
    padding: 68px 0 0 88px;
    color: var(--white);
    font-weight: 700;
    font-size: 64px;
    line-height: 1.18;
    letter-spacing: 1px;
  }
  .card__contact {
    height: 156px;
    background: var(--teal);
    padding: 24px 0 0 90px;
    color: var(--white);
    font-weight: 500;
    font-size: 24px;
    line-height: 1.22;
  }
  .contact-line {
    display: flex;
    align-items: flex-start;
    gap: 8px;
  }
  .contact-line + .contact-line { margin-top: 16px; }
  .contact-line svg {
    flex: none;
    width: 18px;
    height: 22px;
    margin-top: 2px;
    fill: var(--white);
  }
  .card__base { flex: 1; background: var(--navy); }

  /* Back */
  .card--back {
    background: var(--white);
  }
  .brand {
    position: absolute;
    top: 200px;
    left: 0;
    right: 0;
    display: flex;
    align-items: center;
    justify-content: center;
    gap: 16px;
  }
  .brand__dot {
    width: 26px;
    height: 26px;
    border-radius: 50%;
    background: var(--teal);
  }
  .brand__name {
    color: var(--navy);
    font-weight: 400;
    font-size: 48px;
    letter-spacing: 2px;
  }
  .card__stripe {
    position: absolute;
    left: 0;
    right: 0;
    bottom: 39px;
    height: 29px;
    display: flex;
  }
  .card__stripe span { flex: 1; }
  .card__stripe .stripe-navy { background: var(--navy); }
  .card__stripe .stripe-teal { background: var(--teal); }
</style>
</head>
<body>
  <main class="sheet">
    <section class="card card--front" aria-label="Business card front">
      <h1 class="card__name">Dr. CORISANDE<br>THRELKELD Ph.D.</h1>
      <div class="card__contact">
        <p class="contact-line">
          <svg viewBox="0 0 24 24" aria-hidden="true"><path d="M6.6 10.8a15.1 15.1 0 0 0 6.6 6.6l2.2-2.2a1 1 0 0 1 1-.25 11.4 11.4 0 0 0 3.6.57 1 1 0 0 1 1 1V20a1 1 0 0 1-1 1A17 17 0 0 1 3 4a1 1 0 0 1 1-1h3.5a1 1 0 0 1 1 1c0 1.25.2 2.45.57 3.57a1 1 0 0 1-.25 1z"/></svg>
          <span>555.317.0942</span>
        </p>
        <p class="contact-line">
          <svg viewBox="0 0 24 24" aria-hidden="true"><path d="M12 2a7 7 0 0 0-7 7c0 5.25 7 13 7 13s7-7.75 7-13a7 7 0 0 0-7-7zm0 9.5A2.5 2.5 0 1 1 12 6.5a2.5 2.5 0 0 1 0 5z"/></svg>
          <span>QVT Foundry Campus 4417 Foundry Campus Loop<br>Building 2600 Room 314. Baton Rouge LA 70931.</span>
        </p>
      </div>
      <div class="card__base"></div>
    </section>

    <section class="card card--back" aria-label="Business card back">
      <div class="brand">
        <span class="brand__dot"></span>
        <span class="brand__name">MERIDIAN ASSAY</span>
      </div>
      <div class="card__stripe">
        <span class="stripe-navy"></span>
        <span class="stripe-teal"></span>
      </div>
    </section>
  </main>
</body>
</html>
```